CRPG is needing business cards, and stationary created.

Pixel Forge created a logo for our business, and now we are wanting business cards, and stationary. I have included two designs of the same logo. Please feel free to use them as you want. The name of the company is Cedar Ridge Property Group LLC, the address is 812 NE Willow Ln., Suite 9, the city & state is Bend, Oregon, zip code is 97815, Telephone number is 541-327-4489, Fax number is 541-327-6051, the name on the business card is Carl Whitby CMCA

Industry/Entity Type

Property Management

Contact Information for Business Card

The card needs to look professional. Upscale.

Requirements
Must have
• The colors we are using are on the logo that has been uploaded.

```html
<!DOCTYPE html>
<html lang="en">
<head>
<meta charset="utf-8">
<title>Cedar Ridge Property Group – Stationery</title>
<link rel="stylesheet" href="https://fonts.googleapis.com/css2?family=Source+Sans+3:wght@400;600;700&display=swap">
<style>
  :root{
    --teal:#178e7a;
    --teal-light:#1fbba0;
    --slate:#3d4556;
    --paper:#ffffff;
    --ground:#ececec;
    --edge:#7a7f88;
    --ghost:#e2e2e2;
  }
  html,body{margin:0;padding:0;overflow:hidden;}
  body{font-family:"Source Sans 3",sans-serif;}
  .canvas{position:relative;width:1200px;height:1200px;overflow:hidden;
    background:radial-gradient(circle at 30% 50%, #f3f3f3 0%, var(--ground) 70%);}
  .sheet{position:absolute;background:var(--paper);box-sizing:border-box;border:1px solid var(--edge);}
  .brand{position:absolute;display:flex;flex-direction:column;align-items:center;}
  .brand-mark{background:var(--teal);}
  .brand-name{color:var(--teal);font-weight:700;white-space:nowrap;letter-spacing:.02em;line-height:1;text-transform:uppercase;}
  .band{position:absolute;}
  .band svg{display:block;width:100%;height:100%;}
  .contact{position:absolute;color:#fff;text-align:right;white-space:nowrap;}

  /* letterhead */
  .letterhead{left:269px;top:152px;width:661px;height:936px;}
  .letterhead .rule{position:absolute;left:0;right:0;top:94px;height:1px;background:var(--slate);}
  .letterhead .brand{left:0;right:0;top:26px;}
  .letterhead .brand-mark{width:30px;height:30px;margin-bottom:12px;}
  .letterhead .brand-name{font-size:25px;}
  .letterhead .brand-sub{color:var(--slate);font-size:10px;font-weight:600;letter-spacing:.25em;margin-top:4px;background:#fff;padding:0 6px;}
  .letterhead .band{left:274px;top:855px;width:386px;height:63px;}
  .letterhead .contact{right:39px;top:861px;font-size:11.5px;line-height:16px;}

  /* envelope */
  .flap-shadow{position:absolute;left:686px;top:607px;width:100px;height:30px;}
  .envelope{left:437px;top:636px;width:720px;height:320px;border-top:none;border-right:none;}
  .envelope .flap{position:absolute;left:-1px;top:0;width:721px;height:121px;}
  .envelope .brand{left:30px;top:222px;align-items:flex-start;}
  .envelope .brand-mark{width:24px;height:24px;margin:0 0 10px 52px;}
  .envelope .brand-name{font-size:21px;}
  .envelope .brand-sub{color:var(--slate);font-size:8.5px;font-weight:600;letter-spacing:.22em;margin-top:4px;}
  .envelope .ghost-mark{position:absolute;left:538px;top:134px;width:102px;height:112px;background:var(--ghost);}
  .envelope .band{left:373px;top:272px;width:347px;height:48px;}
  .envelope .contact{right:20px;top:273px;font-size:11.5px;line-height:16px;}

  /* business card */
  .card{left:801px;top:453px;width:281px;height:161px;}
  .card .top-bar{position:absolute;left:0;right:0;top:7px;height:9px;
    background:linear-gradient(90deg,var(--teal),var(--teal-light) 50%,var(--teal));}
  .card .brand{left:18px;top:30px;align-items:flex-start;}
  .card .brand-mark{width:20px;height:20px;margin:0 0 8px 40px;}
  .card .brand-name{font-size:15.5px;}
  .card .brand-sub{color:var(--slate);font-size:6.5px;font-weight:600;letter-spacing:.2em;margin-top:3px;}
  .card .person{position:absolute;right:14px;top:54px;text-align:right;line-height:1;}
  .card .person-name{font-size:12.5px;color:var(--slate);}
  .card .person-name strong{color:var(--teal);font-weight:700;}
  .card .person-title{font-size:9px;color:var(--slate);margin-top:2px;}
  .card .band{left:37px;top:113px;width:243px;height:47px;}
  .card .contact{right:14px;top:117px;font-size:8.6px;line-height:10.5px;}
</style>
</head>
<body>
<div class="canvas">
  <svg width="0" height="0" style="position:absolute">
    <defs>
      <linearGradient id="bandFill" x1="0" y1="0" x2="1" y2="0">
        <stop offset="0" stop-color="#178e7a"/>
        <stop offset=".55" stop-color="#1fbba0"/>
        <stop offset="1" stop-color="#178e7a"/>
      </linearGradient>
    </defs>
  </svg>

  <section class="sheet letterhead">
    <div class="rule"></div>
    <div class="brand">
      <div class="brand-mark"></div>
      <div class="brand-name">Cedar Ridge</div>
      <div class="brand-sub">PROPERTY GROUP</div>
    </div>
    <div class="band">
      <svg viewBox="0 0 386 63" preserveAspectRatio="none"><path d="M0,63 C35,63 45,55 65,35 C90,8 110,0 145,0 H386 V63 Z" fill="url(#bandFill)"/></svg>
    </div>
    <div class="contact">812 NE Willow Ln., Suite 9, Bend, Oregon,&nbsp; 97815<br>Tel. 541-327-4489&nbsp; Fax 541-327-6051</div>
  </section>

  <svg class="flap-shadow" viewBox="0 0 100 30"><path d="M0,30 L50,0 L100,30 Z" fill="#dadada"/></svg>
  <section class="sheet envelope">
    <svg class="flap" viewBox="0 0 721 121" preserveAspectRatio="none"><path d="M6,0 H715 Q722,0 721,8 L710,112 Q709,121 698,121 H22 Q12,121 11,112 L1,8 Q0,0 6,0 Z" fill="#178e7a"/></svg>
    <div class="ghost-mark"></div>
    <div class="brand">
      <div class="brand-mark"></div>
      <div class="brand-name">Cedar Ridge</div>
      <div class="brand-sub">PROPERTY GROUP</div>
    </div>
    <div class="band">
      <svg viewBox="0 0 347 48" preserveAspectRatio="none"><path d="M0,48 C25,48 35,42 50,26 C68,6 85,0 110,0 H347 V48 Z" fill="url(#bandFill)"/></svg>
    </div>
    <div class="contact">812 NE Willow Ln., Suite 9, Bend, Oregon,&nbsp; 97815<br>Tel. 541-327-4489&nbsp; Fax 541-327-6051</div>
  </section>

  <section class="sheet card">
    <div class="top-bar"></div>
    <div class="brand">
      <div class="brand-mark"></div>
      <div class="brand-name">Cedar Ridge</div>
      <div class="brand-sub">PROPERTY GROUP</div>
    </div>
    <div class="person">
      <div class="person-name"><strong>Carl</strong>Whitby</div>
      <div class="person-title">CMCA</div>
    </div>
    <div class="band">
      <svg viewBox="0 0 243 47" preserveAspectRatio="none"><path d="M0,47 C22,47 30,42 42,30 C58,12 72,0 100,0 H243 V47 Z" fill="url(#bandFill)"/></svg>
    </div>
    <div class="contact">812 NE Willow Ln., Suite 9,<br>Bend, Oregon,&nbsp; 97815.<br>Tel. 541-327-4489&nbsp; Fax 541-327-6051</div>
  </section>
</div>
</body>
</html>
```